Vending machine company website for SnackHarbor

We need a website for our vending machine services company. It will be based on another website that a friend has. My URL is snackharbor.com and the one I'm trying to emulate with my own logo and colors is pantrybloxo.com.

This will be roughly 6 total pages with one being an opt-in/opt-out page for SMS messages, one being a contact form, etc.

I want to use the logo I purchased from this site that I have attached.

The goal is to be clean, professional, intuitive and easy navigation, etc.

The only difference between my site and the reference site should be that we are not offering coffee service.

I will need all of the code for the site, and it should not use any CMS things like Joomla, Wordpress, etc.

Our actual machines are this model minus the green highlights.f

https://www.kelvomat.com/krx-pdl-mq-snack-and-drink-vending-machine-374.html

Target Market(s)

Companies that want to have vending machine services, or to buy or lease vending machines

Industry/Entity Type

Vending machines for snacks and drinks either placed at locations like apartment complexes, waiting rooms for tire centers, office building break rooms, etc. also vending machine repair services, or selling or leasing vending machines to those interested in getting into the business.

Coding

Coded - Design and coding required

Number of Pages Required

5+ page

Font styles to use
Sans Serif

Requirements
Must have
• It will be similar to pantrybloxo.com in terms of pages, categories, etc. but with our logo, colors, etc. and should be clean and professional. It will have the same pages plus one other page for opt-in or opt-out of SMS messages
Nice to have
• Clean graphics and perhaps some AI designs for vending machine repair, just like the one they use on the pantrybloxo.com site. We would like multiple photos on the home page cycling where you see very attractive people shopping for snacks and drinks at the machines with the items blurred, or people sitting around laughing and smiling while enjoying snacks or drinks at a campus break room, or picnic table, or outside with the machine behind them. Please search for KRX-PDL-47M(B2) Snack And Drink Vending Machine at kelvomat
Should not have
• It can not be designed for CRM like WordPress, Joomla, etc. and should be clean new code, that doesn't attract hackers and it shouldn't be too busy.

```html
<!DOCTYPE html>
<html lang="en">
<head>
<meta charset="utf-8">
<title>SnackHarbor — Vending Services</title>
<link href="https://fonts.googleapis.com/css2?family=Poppins:wght@400;500;600;700&family=Lato:wght@400;700;900&display=swap" rel="stylesheet">
<style>
:root{
  --orange:#e0922f;
  --orange-dark:#c97a1c;
  --brown:#7b5220;
  --ink:#1b1b1b;
  --dark:#252525;
  --grey-card:#f1f1f1;
  --cream:#faf4ec;
  --white:#ffffff;
  --text:#2a2a2a;
}
*{margin:0;padding:0;box-sizing:border-box}
html,body{width:1200px;height:3441px;overflow:hidden}
body{font-family:"Lato",sans-serif;color:var(--text);background:var(--white);position:relative}
.abs{position:absolute}
.poppins{font-family:"Poppins",sans-serif}

/* top nav */
.topnav{left:0;top:0;width:1200px;height:67px;background:var(--dark)}
.topnav a{position:absolute;top:20px;color:var(--white);font-family:"Poppins",sans-serif;font-size:17px;text-decoration:none}
.topnav a.current{border-bottom:1px solid var(--white);padding-bottom:1px}

/* header */
.brand{font-family:"Poppins",sans-serif;font-weight:600;color:var(--orange);font-size:42px;letter-spacing:-0.5px;line-height:1}
.callnow{left:738px;top:78px;font-family:"Lato",sans-serif;font-weight:900;font-size:24px;color:var(--ink);white-space:nowrap}
.callnow b{font-family:"Poppins",sans-serif;font-weight:600;font-size:25px}
.btn-frame{border:3px solid var(--ink);padding:4px}
.btn-frame span{display:flex;align-items:center;justify-content:center;width:100%;height:100%;background:var(--orange);color:var(--white);font-weight:900;font-size:14px}

/* hero */
.hero{left:0;top:179px;width:1200px;height:551px;background:linear-gradient(135deg,#e7a040 0%,#d98c2a 55%,#cf8524 100%);overflow:hidden}
.hero-title{left:596px;top:48px;font-family:"Poppins",sans-serif;font-weight:600;font-size:40px;color:var(--white);white-space:nowrap}
.get-started{left:946px;top:122px;width:140px;height:45px;border:3px solid var(--white);padding:4px}
.get-started span{display:flex;align-items:center;justify-content:center;height:100%;background:var(--orange);color:var(--white);font-weight:900;font-size:13px}
.message-box{left:723px;top:188px;width:367px;height:302px;border:3px solid var(--white);background:var(--brown)}
.message-box h3{text-align:center;margin-top:18px;color:var(--white);font-weight:900;font-size:21px}
.field{position:absolute;height:42px;border:1.5px solid var(--white);color:var(--white);font-size:11px;font-weight:700;display:flex;align-items:center;padding-left:9px}
.field svg{position:absolute;right:12px;top:17px}
.submit{left:830px;top:460px;width:155px;height:47px;background:var(--white);color:var(--orange);font-weight:700;font-size:15px;display:flex;align-items:center;justify-content:center}

/* section labels */
.eyebrow{font-family:"Poppins",sans-serif;font-weight:600;font-size:15px;letter-spacing:3.5px;color:var(--orange)}
.heading{font-family:"Poppins",sans-serif;font-weight:600;font-size:36px;color:var(--ink)}
.center{left:0;width:1200px;text-align:center}

/* about */
.about-text{left:111px;width:515px;font-size:14.5px;line-height:26px;color:var(--text)}
.about-photo{left:686px;top:816px;width:404px;height:347px;border:3px solid var(--orange);background:linear-gradient(180deg,#8fc3ea 0%,#cfe6f3 35%,#3fb8b5 70%,#2b9c9b 100%);box-shadow:0 4px 10px rgba(0,0,0,.25)}

/* products */
.products{left:0;top:1234px;width:1200px;height:569px;background:linear-gradient(180deg,#e0922f 0%,#dd8f2e 100%);overflow:hidden}
.product-card{position:absolute;top:145px;height:335px;background:var(--white)}
.product-card .shot{position:absolute;left:3px;top:3px;right:3px;height:296px}
.product-card .label{position:absolute;left:24px;right:24px;bottom:0;height:53px;background:var(--white);display:flex;align-items:center;justify-content:center;font-size:19px;font-weight:700;color:var(--ink)}
.arrow-btn{position:absolute;top:296px;width:34px;height:34px;border-radius:50%;background:var(--white);display:flex;align-items:center;justify-content:center}

/* testimonials */
.t-card{position:absolute;left:111px;width:337px;background:var(--grey-card)}
.t-card.active{background:var(--white);border:2px solid var(--orange);box-shadow:0 2px 8px rgba(0,0,0,.12)}
.avatar{position:absolute;left:22px;width:64px;height:64px;border-radius:50%;background:radial-gradient(circle at 50% 40%,#b89a86 0%,#6e5648 70%)}
.t-name{position:absolute;left:108px;font-family:"Poppins",sans-serif;font-weight:500;font-size:21px;color:var(--ink)}
.t-name.hl{color:var(--orange);font-weight:600;text-transform:uppercase;font-size:20px}
.t-role{position:absolute;left:108px;font-family:"Poppins",sans-serif;font-weight:500;font-size:11.5px;color:#333}
.quote{left:557px;width:520px;font-size:14.5px;line-height:31px;color:var(--text)}

/* services */
.services{left:0;top:2385px;width:1200px;height:582px;background:var(--cream)}
.service-card{position:absolute;top:143px;width:297px;height:368px;background:var(--white)}
.service-card .shot{position:absolute;left:0;top:0;width:297px;height:321px}
.service-card .label{position:absolute;left:22px;right:22px;top:292px;height:76px;background:var(--white);text-align:center;font-size:19px;font-weight:700;line-height:28px;color:var(--ink);padding-top:10px}

/* footer */
.footer{left:0;top:2967px;width:1200px;height:474px;background:var(--dark);color:var(--white)}
.footer h4{position:absolute;font-weight:700;font-size:20px}
.footer .small{position:absolute;font-size:12.5px;line-height:26px}
.f-icon{position:absolute;left:736px;width:35px;height:35px;background:var(--orange);display:flex;align-items:center;justify-content:center}
.f-line{position:absolute;left:780px;font-size:15px;line-height:27px}
.quick{position:absolute;left:971px;font-size:15px;display:flex;align-items:center;gap:10px}
</style>
</head>
<body>

<!-- top navigation -->
<nav class="abs topnav">
  <a class="current" style="left:155px">Home</a>
  <a style="left:320px">Our Machines</a>
  <a style="left:561px">Services</a>
  <a style="left:756px">Products</a>
  <a style="left:951px">Contact Us</a>
</nav>

<!-- header -->
<header>
  <div class="abs brand" style="left:114px;top:98px">SnackHarbor</div>
  <div class="abs callnow">CALL NOW: <b>+1 555 014 2277</b></div>
  <div class="abs btn-frame" style="left:715px;top:116px;width:195px;height:46px"><span>SCHEDULE SERVICE</span></div>
  <div class="abs btn-frame" style="left:945px;top:116px;width:142px;height:46px"><span>CONTACT NOW</span></div>
</header>

<!-- hero -->
<section class="abs hero">
  <svg class="abs" style="left:0;top:0" width="1200" height="551" aria-hidden="true">
    <polygon points="830,0 1200,0 1200,300" fill="#d88a28" opacity=".45"/>
    <polygon points="1200,360 1200,551 980,551" fill="#c97f22" opacity=".4"/>
  </svg>
  <div class="abs" role="img" aria-label="Woman with glasses holding a coffee cup, choosing from a vending machine" style="left:0;top:0;width:730px;height:551px;clip-path:polygon(0 0,548px 0,722px 551px,0 551px);background:linear-gradient(120deg,#5a5550 0%,#9a9590 35%,#d9d5cf 60%,#ece8e2 100%)"></div>
  <div class="abs hero-title">Welcome to SnackHarbor</div>
  <div class="abs get-started"><span>GET STARTED</span></div>
  <form class="abs message-box">
    <h3>SEND US A MESSAGE</h3>
  </form>
  <div class="field" style="left:740px;top:243px;width:333px">Name of location<svg width="10" height="6"><polygon points="0,0 10,0 5,6" fill="#fff"/></svg></div>
  <div class="field" style="left:740px;top:295px;width:333px">No of machines<svg width="10" height="6"><polygon points="0,0 10,0 5,6" fill="#fff"/></svg></div>
  <div class="field" style="left:740px;top:348px;width:158px">Machine Option<svg width="10" height="6"><polygon points="0,0 10,0 5,6" fill="#fff"/></svg></div>
  <div class="field" style="left:914px;top:348px;width:159px">Name</div>
  <div class="field" style="left:740px;top:400px;width:158px">Email</div>
  <div class="field" style="left:914px;top:400px;width:159px">Phone Number</div>
  <div class="abs submit">SUBMIT</div>
</section>

<!-- about -->
<section>
  <div class="abs" style="left:800px;top:893px;width:400px;height:341px;background:var(--dark)"></div>
  <div class="abs eyebrow" style="left:111px;top:800px">WHO WE ARE</div>
  <h2 class="abs heading" style="left:111px;top:826px">About SnackHarbor</h2>
  <p class="abs about-text" style="top:873px">Nam libero tempore, cum soluta nobis est eligendi optio cumque nihil impedit quo minus id quod maxime placeat facere possimus, omnis voluptas assumenda est, omnis dolor repellendus. Temporibus autem quibusdam et aut officiis debitis aut rerum necessitatibus saepe eveniet ut et voluptates repudiandae sint et molestiae non recusandae.</p>
  <p class="abs about-text" style="top:1027px">Itaque earum rerum hic tenetur a sapiente delectus, ut aut reiciendis voluptatibus maiores alias consequatur aut perferendis doloribus asperiores repellat.</p>
  <div class="abs btn-frame" style="left:111px;top:1121px;width:143px;height:46px"><span>READ MORE</span></div>
  <div class="abs about-photo" role="img" aria-label="Aerial view of a marina with yachts and high-rise towers"></div>
</section>

<!-- products -->
<section class="abs products">
  <div class="abs" style="left:0;top:0;width:1200px;height:569px;background:linear-gradient(180deg,rgba(0,0,0,0) 40%,rgba(150,90,20,.18) 100%)"></div>
  <div class="abs eyebrow center" style="top:48px;color:var(--white)">VENDING</div>
  <h2 class="abs heading center" style="top:72px;color:var(--white)">Our Products</h2>

  <div class="product-card" style="left:111px;width:222px">
    <div class="shot" role="img" aria-label="Woman choosing snacks at a vending machine" style="background:linear-gradient(135deg,#2b3b7a,#7a6a5a 60%,#d9cbb8)"></div>
    <div class="label">Snacks</div>
  </div>
  <div class="product-card" style="left:365px;width:218px">
    <div class="shot" role="img" aria-label="Finger pressing the keypad of a drinks machine" style="background:linear-gradient(135deg,#8fa89a,#3a3a3a 55%,#1a1a1a)"></div>
    <div class="label">Drinks</div>
  </div>
  <div class="product-card" style="left:615px;width:222px">
    <div class="shot" role="img" aria-label="Coin being inserted into a red laundry machine" style="background:linear-gradient(135deg,#e4665a,#c94a3f 55%,#9a8a7a)"></div>
    <div class="label">Laundry Products</div>
  </div>
  <div class="product-card" style="left:869px;width:217px">
    <div class="shot" role="img" aria-label="Row of stocked vending machines" style="background:linear-gradient(180deg,#bfbfbf,#4a4a4a 45%,#d6d6d6)"></div>
    <div class="label">Healthy</div>
  </div>

  <div class="arrow-btn" style="left:32px"><svg width="10" height="14"><polyline points="8,1 2,7 8,13" fill="none" stroke="#c97a1c" stroke-width="2.2"/></svg></div>
  <div class="arrow-btn" style="left:1130px"><svg width="10" height="14"><polyline points="2,1 8,7 2,13" fill="none" stroke="#c97a1c" stroke-width="2.2"/></svg></div>
</section>

<!-- testimonials -->
<section>
  <div class="abs eyebrow center" style="top:1852px">TESTIMONIALS</div>
  <h2 class="abs heading center" style="top:1878px">What Customer Says</h2>

  <div class="t-card" style="top:1958px;height:97px">
    <div class="avatar" role="img" aria-label="Customer portrait" style="top:16px"></div>
    <div class="t-name" style="top:24px">Dana Morrow</div>
    <div class="t-role" style="top:62px">Senior Manager, United States</div>
  </div>
  <div class="t-card active" style="top:2077px;height:100px">
    <div class="avatar" role="img" aria-label="Customer portrait" style="top:16px"></div>
    <div class="t-name hl" style="top:24px">Omar Belkadi</div>
    <div class="t-role" style="top:62px">Assistant Manager, United States</div>
  </div>
  <div class="t-card" style="top:2206px;height:98px">
    <div class="avatar" role="img" aria-label="Customer portrait" style="top:17px"></div>
    <div class="t-name" style="top:25px">Dana Morrow</div>
    <div class="t-role" style="top:63px">Senior Manager, United States</div>
  </div>

  <div class="abs poppins" style="left:557px;top:1952px;font-weight:500;font-size:23px;color:var(--ink)">Omar Belkadi <span style="font-size:11.5px;color:#555;margin-left:8px">(Assistant Manager, United States)</span></div>
  <svg class="abs" style="left:557px;top:1999px" width="90" height="18" aria-label="Five stars">
    <g fill="#f2a62f">
      <polygon points="8,0 10.4,5.6 16,6.1 11.7,9.8 13,15.5 8,12.5 3,15.5 4.3,9.8 0,6.1 5.6,5.6"/>
      <polygon transform="translate(18,0)" points="8,0 10.4,5.6 16,6.1 11.7,9.8 13,15.5 8,12.5 3,15.5 4.3,9.8 0,6.1 5.6,5.6"/>
      <polygon transform="translate(36,0)" points="8,0 10.4,5.6 16,6.1 11.7,9.8 13,15.5 8,12.5 3,15.5 4.3,9.8 0,6.1 5.6,5.6"/>
      <polygon transform="translate(54,0)" points="8,0 10.4,5.6 16,6.1 11.7,9.8 13,15.5 8,12.5 3,15.5 4.3,9.8 0,6.1 5.6,5.6"/>
      <polygon transform="translate(72,0)" points="8,0 10.4,5.6 16,6.1 11.7,9.8 13,15.5 8,12.5 3,15.5 4.3,9.8 0,6.1 5.6,5.6"/>
    </g>
  </svg>
  <p class="abs quote" style="top:2029px">Temporibus autem quibusdam et aut officiis debitis aut rerum necessitatibus saepe eveniet ut et voluptates repudiandae sint et molestiae non recusandae.</p>
  <p class="abs quote" style="top:2122px">Itaque earum rerum hic tenetur a sapiente delectus, ut aut reiciendis voluptatibus maiut officiis debitis aut rerum necessitatibus saepe eveniet ut a sapiente delectus, ut aut reiciendis voluptatibusores alias consequatur aut perferendis doloribus asperiores repellat.</p>
  <div class="abs" style="left:557px;top:2260px;font-weight:700;font-size:17px;color:var(--orange)">Thanks, SnackHarbor</div>
</section>

<!-- services -->
<section class="abs services">
  <div class="abs eyebrow center" style="top:50px">SERVICES</div>
  <h2 class="abs heading center" style="top:75px">What We Do</h2>

  <div class="service-card" style="left:111px">
    <div class="shot" role="img" aria-label="Stocked snack vending machine with green trim" style="background:linear-gradient(90deg,#2a2a2a,#7a6f66 40%,#c9a070 60%,#4aa24a)"></div>
    <div class="label">Vending Machine<br>Placement</div>
  </div>
  <div class="service-card" style="left:452px">
    <div class="shot" role="img" aria-label="Smiling technician refilling a machine" style="background:linear-gradient(135deg,#e8e8e8,#c4c4c4 45%,#6e2a2a 70%,#2a2a2a)"></div>
    <div class="label">Bi-weekly or Monthly<br>Refill Service</div>
  </div>
  <div class="service-card" style="left:792px">
    <div class="shot" role="img" aria-label="Hand touching a glowing customer-satisfaction rating on a screen" style="background:radial-gradient(circle at 45% 45%,#f0a040 0%,#3a6e96 35%,#0f2a44 80%)"></div>
    <div class="label">Ongoing Customer<br>Support</div>
  </div>
</section>

<!-- footer -->
<footer class="abs footer">
  <div class="abs brand" style="left:118px;top:97px;font-size:38px">SnackHarbor</div>

  <h4 style="left:446px;top:89px">Subscribe Us</h4>
  <p class="small" style="left:446px;top:126px;width:230px">Itaque earum rerum hic tenetur a voluptatibus maiores aliasr</p>
  <div class="abs" style="left:446px;top:188px;width:229px;height:47px;background:var(--white);color:#888;font-size:12.5px;display:flex;align-items:center;padding-left:18px">Enter The Email</div>
  <div class="abs" style="left:446px;top:255px;width:185px;height:55px;background:var(--orange);font-weight:700;font-size:17px;display:flex;align-items:center;padding-left:19px">Subscribe</div>

  <h4 style="left:736px;top:89px">Contact Us</h4>
  <div class="f-icon" style="top:131px"><svg width="14" height="18"><path d="M7 1C3.7 1 1.5 3.4 1.5 6.4 1.5 10.5 7 17 7 17s5.5-6.5 5.5-10.6C12.5 3.4 10.3 1 7 1z" fill="#fff"/><circle cx="7" cy="6.4" r="2.2" fill="#e0922f"/></svg></div>
  <div class="f-line" style="top:128px">SnackHarbor<br>United State</div>
  <div class="f-icon" style="top:202px"><svg width="16" height="16"><path d="M3.5 1.5l3 3-1.8 1.8c.8 1.9 2.4 3.5 4.3 4.3l1.8-1.8 3 3-1.8 2C7 13.6 2.4 9 1.5 3.3z" fill="#fff"/></svg></div>
  <div class="f-line" style="top:206px">+1 555 014 2277</div>
  <div class="f-icon" style="top:270px"><svg width="16" height="12"><rect x="0.5" y="0.5" width="15" height="11" fill="#fff"/><polyline points="1,1 8,7 15,1" fill="none" stroke="#e0922f" stroke-width="1.4"/></svg></div>
  <div class="f-line" style="top:274px">info@snackharbor.com</div>

  <h4 style="left:971px;top:89px">Quick Links</h4>
  <div class="quick" style="top:135px"><svg width="13" height="12"><path d="M0 6h10M6 1.5l4.5 4.5L6 10.5" fill="none" stroke="#fff" stroke-width="2"/></svg>Home</div>
  <div class="quick" style="top:169px"><svg width="13" height="12"><path d="M0 6h10M6 1.5l4.5 4.5L6 10.5" fill="none" stroke="#fff" stroke-width="2"/></svg>About</div>
  <div class="quick" style="top:203px"><svg width="13" height="12"><path d="M0 6h10M6 1.5l4.5 4.5L6 10.5" fill="none" stroke="#fff" stroke-width="2"/></svg>Services</div>
  <div class="quick" style="top:237px"><svg width="13" height="12"><path d="M0 6h10M6 1.5l4.5 4.5L6 10.5" fill="none" stroke="#fff" stroke-width="2"/></svg>Products</div>
  <div class="quick" style="top:271px"><svg width="13" height="12"><path d="M0 6h10M6 1.5l4.5 4.5L6 10.5" fill="none" stroke="#fff" stroke-width="2"/></svg>Contact Us</div>

  <div class="abs" style="left:111px;top:376px;width:978px;height:1px;background:#9a9a9a"></div>
  <div class="abs" style="left:0;top:412px;width:1200px;text-align:center;font-size:13.5px">Copyrights@2024.SnackHarbor.All Rights Reserved</div>
</footer>

</body>
</html>
```